Mesh Banner Design for Business Premises

We require the design of a large mesh banner to be installed across the front fence of our warehouse. The banner should prominently feature our existing Trelborn logo and brand colours (yellow, white, and black) and be designed to be highly visible from the road.

The overall aesthetic should be strong, masculine, and industrial, reflecting the nature of the scaffolding and construction industry. The background should be predominantly black, with our branding incorporated in yellow and white for strong contrast and readability.

The banner should clearly communicate the full scope of services we provide, including:

Scaffold Design
Scaffold Engineering
Scaffold Installation / Erection
Scaffold Dismantling

It should also indicate the types of projects and clients we service, including:

Commercial
Industrial
Residential
Civil

The design should feel bold and professional, with a construction-oriented style that aligns with the scaffolding industry. It should be clean, impactful, and easy to read from a distance, ensuring passing traffic can quickly understand our services.

Where possible, subtle industrial or structural design elements (such as scaffold components, steel textures, or linework) may be incorporated into the background to reinforce the industry theme while keeping the layout uncluttered.

The final design will be produced as a large-format mesh banner for outdoor installation, so it should be created with this application and viewing distance in mind.

```html
<!DOCTYPE html>
<html lang="en">
<head>
<meta charset="utf-8">
<title>Trelborn Mesh Banner</title>
<link rel="stylesheet" href="https://fonts.googleapis.com/css2?family=Montserrat:wght@600;700;800&display=swap">
<style>
  :root {
    --banner-black: #141414;
    --steel-dark: #1c1d1f;
    --steel-mid: #34363a;
    --brand-yellow: #f2b705;
    --brand-white: #f2f2f0;
  }
  * { margin: 0; padding: 0; box-sizing: border-box; }
  html, body { width: 800px; height: 1200px; overflow: hidden; background: var(--banner-black); }
  .banner {
    position: relative;
    width: 800px;
    height: 1200px;
    overflow: hidden;
    font-family: "Montserrat", sans-serif;
    color: var(--brand-white);
  }
  .steel-backdrop {
    position: absolute; inset: 0;
    background:
      radial-gradient(ellipse at 50% 22%, rgba(90,92,96,0.35), transparent 60%),
      linear-gradient(180deg, var(--steel-mid) 0%, var(--steel-dark) 45%, #202124 75%, var(--banner-black) 100%);
  }
  .brand-mark-square {
    position: absolute; top: 70px; left: 285px;
    width: 230px; height: 230px;
    border: 8px solid var(--brand-yellow);
  }
  .brand-name {
    position: absolute; top: 322px; left: 0; width: 100%;
    text-align: center; line-height: 1;
    font-weight: 700; font-size: 64px; letter-spacing: 12px;
    color: var(--brand-white); text-transform: uppercase;
  }
  .rule { position: absolute; height: 4px; background: var(--brand-yellow); }
  .rule--top { top: 418px; left: 40px; width: 720px; }
  .rule--mid { top: 540px; left: 0; width: 800px; }
  .rule--low { top: 918px; left: 40px; width: 720px; }
  .phone {
    position: absolute; left: 0; width: 100%; text-align: center;
    font-weight: 800; color: var(--brand-yellow); letter-spacing: 1px; line-height: 1;
  }
  .phone--primary { top: 442px; font-size: 76px; }
  .phone--secondary { top: 945px; font-size: 84px; }
  .service-list {
    position: absolute; top: 578px; list-style: none;
    font-weight: 600; font-size: 30px; line-height: 1.22;
  }
  .service-list--scope { left: 50px; width: 400px; }
  .service-list--sectors { left: 462px; width: 320px; }
  .service-item { position: relative; padding-left: 56px; margin-bottom: 8px; }
  .service-list--sectors .service-item { margin-bottom: 14px; padding-left: 50px; }
  .tick { position: absolute; left: 0; top: 6px; width: 36px; height: 28px; }
  .hazard-band {
    position: absolute; left: 0; top: 1065px; width: 800px; height: 46px;
    background: repeating-linear-gradient(-60deg,
      var(--brand-yellow) 0 30px, var(--banner-black) 30px 70px);
  }
</style>
</head>
<body>
<main class="banner">
  <div class="steel-backdrop" role="img" aria-label="Dark riveted steel plates and scaffold tube structure"></div>

  <div class="brand-mark-square"></div>
  <p class="brand-name">Trelborn</p>

  <div class="rule rule--top"></div>
  <p class="phone phone--primary">1300 9 RAISE</p>
  <div class="rule rule--mid"></div>

  <ul class="service-list service-list--scope">
    <li class="service-item"><svg class="tick" viewBox="0 0 38 30"><polyline points="3,15 14,26 35,4" fill="none" stroke="#f2b705" stroke-width="5" stroke-linecap="round" stroke-linejoin="round"/></svg>Scaffold Design</li>
    <li class="service-item"><svg class="tick" viewBox="0 0 38 30"><polyline points="3,15 14,26 35,4" fill="none" stroke="#f2b705" stroke-width="5" stroke-linecap="round" stroke-linejoin="round"/></svg>Scaffold<br>Engineering</li>
    <li class="service-item"><svg class="tick" viewBox="0 0 38 30"><polyline points="3,15 14,26 35,4" fill="none" stroke="#f2b705" stroke-width="5" stroke-linecap="round" stroke-linejoin="round"/></svg>Scaffold<br>Installation /<br>Erection</li>
    <li class="service-item"><svg class="tick" viewBox="0 0 38 30"><polyline points="3,15 14,26 35,4" fill="none" stroke="#f2b705" stroke-width="5" stroke-linecap="round" stroke-linejoin="round"/></svg>Scaffold<br>Dismantling</li>
  </ul>

  <ul class="service-list service-list--sectors">
    <li class="service-item"><svg class="tick" viewBox="0 0 38 30"><polyline points="3,15 14,26 35,4" fill="none" stroke="#f2b705" stroke-width="5" stroke-linecap="round" stroke-linejoin="round"/></svg>Commercial</li>
    <li class="service-item"><svg class="tick" viewBox="0 0 38 30"><polyline points="3,15 14,26 35,4" fill="none" stroke="#f2b705" stroke-width="5" stroke-linecap="round" stroke-linejoin="round"/></svg>Industrial</li>
    <li class="service-item"><svg class="tick" viewBox="0 0 38 30"><polyline points="3,15 14,26 35,4" fill="none" stroke="#f2b705" stroke-width="5" stroke-linecap="round" stroke-linejoin="round"/></svg>Residential</li>
    <li class="service-item"><svg class="tick" viewBox="0 0 38 30"><polyline points="3,15 14,26 35,4" fill="none" stroke="#f2b705" stroke-width="5" stroke-linecap="round" stroke-linejoin="round"/></svg>Civil</li>
  </ul>

  <div class="rule rule--low"></div>
  <p class="phone phone--secondary">1300 9 RAISE</p>

  <div class="hazard-band"></div>
</main>
</body>
</html>
```